Vostrel Holdings Web Design

Vostrel Holdings Limited Shenzhen

This project is a 10 page launch website.
Our client is seeking a contemporary homepage design for a Holdings company. Once we are happy with the homepage design and select designer we will request a secondary page design.

Please see attached company LOGO for an idea of style, it incorporates the traditional Chinese furniture lattice work. The Quillmoor website is one of our clients favorite so we would like to see a similar homepage design to this website.

Use the websites below for reference purpose. The first two are Chinese and the second two are international. We would like to see elements of both but more focus on international design.

http://www.evergrande.com/http://www.brevandgroup.com/pub/default.aspx http://www.quillmoor.com/zh/maldives_resortone/
http://www.vellune-studio.com
http://media-cache-ec0.fotrelix.com/originals/41/a3/90/41a390c1f5b7d2e8a6c4f0b9e3d71a55.jpg

Company Background
VOSTREL HOLDINGS, located in Qianhai, China, is a new real-estate project operator, structuring urban-rural real-estate investment and development, and industrial fund investment. The company also invests in supply chain management and supporting infrastructures. To create new spaces and livable cities Vostrel Holdings develop win-win strategic partnerships with a number of institutions. Currently cooperating with Harrow East Lindcombe, China urban and rural integrated demonstration.

Target Market(s)

B2B property investment. Target market customers are senior level management/decision makers of large corporations. Focusing geographically on the domestic market first and expanding internationally in 2nd and 3rd years.

Industry/Entity Type

Investment

Requirements
Must have
• Since this is a new company, we would like to the website representing growth and power, E.g. like a growing tree.
Should not have
• Low-level vectors such as curency symbols, American dollar.

```html
<!DOCTYPE html>
<html lang="en">
<head>
<meta charset="utf-8">
<title>Vostrel Holdings</title>
<link href="https://fonts.googleapis.com/css2?family=Roboto:wght@400;500;700&family=Roboto+Condensed:wght@400;700&display=swap" rel="stylesheet">
<style>
:root{
  --gold:#c39a45;
  --gold-dark:#b08a3a;
  --ink:#444;
  --body:#333;
  --nav:#555;
  --line:#dcdcdc;
  --footer:#333;
  --footer-line:#444;
  --white:#fff;
  --blue:#2b8de3;
}
*{margin:0;padding:0;box-sizing:border-box}
html,body{width:804px;height:1200px;overflow:hidden;background:var(--white)}
body{position:relative;font-family:"Roboto",Arial,sans-serif;color:var(--body)}
.abs{position:absolute}

/* header */
.brand-mark{left:80px;top:15px;width:64px;height:64px;border:2px solid var(--gold);border-radius:50%}
.brand-name{left:56px;top:82px;font-family:"Roboto",Arial,sans-serif;font-size:13px;font-weight:500;color:var(--gold);letter-spacing:.3px}
.search{left:500px;top:24px;width:174px;height:24px;border:1px solid #d4d4d4;font-size:10px;color:#888;padding:6px 8px}
.search svg{position:absolute;right:7px;top:6px}
.lang{left:705px;top:30px;font-size:10px;color:#333}
.lang svg{margin-left:6px;vertical-align:1px}
.nav{top:78px;font-size:11.5px;font-weight:500;color:var(--nav);letter-spacing:.2px}
.nav.active{color:var(--gold)}
.nav-mark{left:324px;top:111px;width:41px;height:3px;background:var(--gold)}
.nav-mark::after{content:"";position:absolute;left:16px;top:-4px;border:4px solid transparent;border-bottom-color:var(--gold);border-top:0}

/* hero */
.hero{left:0;top:115px;width:804px;height:333px;background:linear-gradient(100deg,#b9e1e6 0%,#a9dbe0 45%,#c9e6ea 100%)}
.hero-plant{left:160px;top:20px;width:280px;height:260px;background:radial-gradient(ellipse at 50% 75%,#6fb43c 0%,#8fc463 35%,rgba(185,225,230,0) 70%)}
.hero-hands{left:380px;top:90px;width:424px;height:243px;background:radial-gradient(ellipse at 60% 55%,#e8bca0 0%,#dfb49a 35%,rgba(185,225,230,0) 72%)}
.hero-caption{left:374px;top:224px;width:371px;height:43px;background:rgba(100,110,112,.8);color:var(--white);font-size:17.5px;line-height:43px;text-align:center;letter-spacing:.2px}
.hero-dots{left:712px;top:429px;display:flex;gap:3px}
.hero-dots span{width:7px;height:7px;border-radius:50%;background:#333;border:1px solid #333}
.hero-dots span:first-child{background:var(--white)}

/* services */
.service{width:200px;text-align:center}
.service-icon{position:relative;margin:0 auto;width:98px;height:98px;border-radius:50%;background:radial-gradient(circle at 50% 40%,#fff 0%,#f1f1f1 55%,#dcdcdc 100%);box-shadow:0 4px 8px rgba(0,0,0,.08)}
.service-icon svg{position:absolute;left:24px;top:24px}
.service h3{margin-top:10px;font-size:14px;font-weight:500;color:var(--gold)}
.service p{margin-top:5px;font-size:9.6px;line-height:16px;color:var(--body)}

.divider{left:84px;top:723px;width:635px;height:1px;background:var(--line)}
.divider::before,.divider::after{content:"";position:absolute;top:-4px;width:9px;height:9px;border-radius:50%;background:#d6d6d6}
.divider::before{left:0}.divider::after{right:0}

.section-title{left:0;top:754px;width:804px;text-align:center;font-family:"Roboto Condensed",Arial,sans-serif;font-size:18.5px;color:var(--ink)}

/* partner cards */
.card-frame{width:153px;height:117px;background:var(--white);border:1px solid #e2e2e2;box-shadow:0 1px 3px rgba(0,0,0,.12);padding:4px}
.card-photo{width:100%;height:100%}
.photo-mono{background:linear-gradient(180deg,#8f8f8f 0%,#6b6b6b 50%,#4c4c4c 100%)}
.photo-color{background:linear-gradient(180deg,#6d9cd4 0%,#9dbce0 35%,#e8dcc0 55%,#c9b893 75%,#3c4650 100%)}
.card-text{width:165px}
.card-text h4{font-size:10px;font-weight:400;color:var(--gold);line-height:12px}
.card-text p{margin-top:7px;font-size:9px;line-height:17px;color:var(--body)}

/* footer */
.footer{left:0;top:970px;width:804px;height:230px;background:var(--footer);color:var(--white)}
.footer h5{position:absolute;top:30px;font-size:10.5px;font-weight:500;letter-spacing:.2px}
.footer ul{position:absolute;top:54px;list-style:none;font-size:9.6px;line-height:19.3px;color:#e6e6e6}
.newsletter-copy{position:absolute;left:338px;top:50px;width:230px;font-size:9.6px;line-height:19px;color:#e6e6e6}
.email{position:absolute;left:338px;top:96px;width:224px;height:23px;background:var(--white);color:#888;font-size:9.6px;padding:6px 7px}
.subscribe{position:absolute;left:485px;top:131px;width:77px;height:27px;background:var(--blue);color:var(--white);font-size:11px;line-height:27px;text-align:center}
.social{position:absolute;top:57px;width:25px;height:25px}
.social.blue-dark{background:#3b5aa6}
.social.blue-light{background:#2a9ce0}
.social.orange{background:#f26d18}
.social.red{background:#e02a2e}
.footer-rule{position:absolute;left:0;top:177px;width:804px;height:1px;background:var(--footer-line)}
.copyright{position:absolute;left:59px;top:195px;font-size:9.6px;color:#e6e6e6}
</style>
</head>
<body>

<header>
  <div class="abs brand-mark"></div>
  <div class="abs brand-name">VOSTREL HOLDINGS</div>
  <div class="abs search">Search..
    <svg width="10" height="10" viewBox="0 0 10 10"><circle cx="4" cy="4" r="3" fill="none" stroke="#999" stroke-width="1.4"/><line x1="6.2" y1="6.2" x2="9" y2="9" stroke="#999" stroke-width="1.6"/></svg>
  </div>
  <div class="abs lang">ENG<svg width="8" height="5" viewBox="0 0 8 5"><path d="M1 1l3 3 3-3" fill="none" stroke="#888" stroke-width="1.5"/></svg></div>
  <nav>
    <span class="abs nav active" style="left:328px">HOME</span>
    <span class="abs nav" style="left:399px">ABOUT US</span>
    <span class="abs nav" style="left:495px">SERVICES</span>
    <span class="abs nav" style="left:589px">PRODUCTS</span>
    <span class="abs nav" style="left:690px">CONTACT</span>
  </nav>
  <div class="abs nav-mark"></div>
</header>

<section class="abs hero">
  <div class="abs hero-plant" role="img" aria-label="Young green sapling growing from a patch of grass on a smartphone held in a hand"></div>
  <div class="abs hero-hands" role="img" aria-label="A second hand reaching toward the phone with a pointing finger"></div>
  <div class="abs hero-caption">SUNT IN CULPA QUI OFFICIA DESERUNT</div>
  <div class="abs hero-dots"><span></span><span></span><span></span><span></span></div>
</section>

<section>
  <div class="abs service" style="left:80px;top:487px">
    <div class="service-icon">
      <svg width="50" height="50" viewBox="0 0 50 50"><path d="M2 16h10l10-5 8 3 8-3h10v16h-8l-12 12c-2 2-5 1-6-1l-2 1c-2 0-3-2-3-3l-2 0c-2 0-3-2-2-4l-2 0c-2 0-3-3-1-4l-8-6z" fill="var(--gold)"/><path d="M22 18l6 3" stroke="#f2f2f2" stroke-width="2"/></svg>
    </div>
    <h3>Investment</h3>
    <p>Vivamus vel gt magat sagittis.<br>Nulla faucibus nibh a agna tint accumsan<br>hendreritacilisis. Curabitur et libero sit<br>amet ante hendrerit</p>
  </div>
  <div class="abs service" style="left:303px;top:487px">
    <div class="service-icon">
      <svg width="50" height="50" viewBox="0 0 50 50"><rect x="10" y="4" width="30" height="42" rx="4" fill="var(--gold)"/><rect x="14" y="8" width="22" height="9" fill="#f2f2f2"/><g fill="#f2f2f2"><rect x="14" y="21" width="6" height="5"/><rect x="22" y="21" width="6" height="5"/><rect x="30" y="21" width="6" height="5"/><rect x="14" y="29" width="6" height="5"/><rect x="22" y="29" width="6" height="5"/><rect x="30" y="29" width="6" height="5"/><rect x="14" y="37" width="6" height="5"/><rect x="22" y="37" width="6" height="5"/><rect x="30" y="37" width="6" height="5"/></g></svg>
    </div>
    <h3>Planning</h3>
    <p>Vivamus vel gt magat sagittis.<br>Nulla faucibus nibh a agna tint accumsan<br>hendreritacilisis. Curabitur et libero sit<br>amet ante hendrerit</p>
  </div>
  <div class="abs service" style="left:526px;top:487px">
    <div class="service-icon">
      <svg width="50" height="50" viewBox="0 0 50 50"><path d="M25 4l20 9-20 9-20-9z" fill="var(--gold)"/><path d="M5 16l18 8v22l-18-8z" fill="var(--gold-dark)"/><path d="M45 16l-18 8v22l18-8z" fill="var(--gold)"/></svg>
    </div>
    <h3>Analysis</h3>
    <p>Vivamus vel gt magat sagittis.<br>Nulla faucibus nibh a agna tint accumsan<br>hendreritacilisis. Curabitur et libero sit<br>amet ante hendrerit</p>
  </div>
</section>

<div class="abs divider"></div>
<h2 class="abs section-title">WE DEVELOP WIN-WIN STRATEGIC PARTNERSHIPS</h2>

<section>
  <div class="abs card-frame" style="left:59px;top:808px">
    <div class="card-photo photo-mono" role="img" aria-label="Black and white photo of a large multi-storey residential house"></div>
  </div>
  <div class="abs card-text" style="left:223px;top:816px">
    <h4>Donec dictum soinidales ligula vel</h4>
    <p>Lorem ipsum dolor sit amet, conuitetr adipisicing elit, sed do eiusinmodtipor Morbi blandit feiuingiat lobortis. Cuiur vel massa ac felis tempus pulvinar id ante. Aliquam et enim mauris.</p>
  </div>
  <div class="abs card-frame" style="left:425px;top:808px">
    <div class="card-photo photo-color" role="img" aria-label="Photo of a cream-coloured townhouse development under a blue sky"></div>
  </div>
  <div class="abs card-text" style="left:589px;top:816px">
    <h4>Donec dictum soinidales ligula vel</h4>
    <p>Lorem ipsum dolor sit amet, conuitetr adipisicing elit, sed do eiusinmodtipor Morbi blandit feiuingiat lobortis. Cuiur vel massa ac felis tempus pulvinar id ante. Aliquam et enim mauris.</p>
  </div>
</section>

<footer class="abs footer">
  <h5 style="left:59px">COMPANY</h5>
  <ul style="left:60px"><li>About us</li><li>What we do?</li><li>Forums</li><li>Support</li><li>Blog</li></ul>
  <h5 style="left:198px">ABOUT US</h5>
  <ul style="left:199px"><li>Vostrel Holdings</li><li>Contact Us</li><li>Help</li><li>Privacy Policy</li><li>Terms Of Service</li></ul>
  <h5 style="left:338px">NEWSLETTER SIGNUP</h5>
  <p class="newsletter-copy">Stay in touch with us by signing up for our quarterly newsletter!</p>
  <div class="email">Enter Email Id</div>
  <div class="subscribe">SUBSCRIBE</div>
  <h5 style="left:620px">FOLLOW US ON</h5>
  <div class="social blue-dark" style="left:619px"></div>
  <div class="social blue-light" style="left:651px"></div>
  <div class="social orange" style="left:684px"></div>
  <div class="social red" style="left:717px"></div>
  <div class="footer-rule"></div>
  <p class="copyright">Copyright ©2013. All Rights Reserved.</p>
</footer>

</body>
</html>
```